"VelTra" - Ketamine Clinic - Save Minds and Heal Hearts!! -

I need a very nice modern happy brain themed warm website design for our cutting edge modern and caring ketamine IV infusion clinic that also offers talk therapy and telemedicine visits.
A great design using the color schemes in out logos (grey, white, purples and that need metallic fading colored effect in the logo).

```html
<!DOCTYPE html>
<html lang="en">
<head>
<meta charset="utf-8">
<title>VelTra – Ketamine Clinic</title>
<link href="https://fonts.googleapis.com/css2?family=Montserrat:wght@400;500;600;700&family=Roboto+Condensed:wght@700&family=Kaushan+Script&display=swap" rel="stylesheet">
<style>
:root{
  --blue:#1a8fe6;
  --purple:#5a08c2;
  --violet:#7b2ff0;
  --grad:linear-gradient(90deg,#1a8fe6 0%,#4a2ad6 55%,#5a08c2 100%);
  --heading:#666666;
  --text:#2b2b2b;
  --muted:#888;
  --grey-bg:#f2f2f2;
  --rule:#777;
  --black:#000;
  --white:#fff;
}
*{margin:0;padding:0;box-sizing:border-box}
html,body{width:1200px;height:4357px;overflow:hidden}
body{font-family:"Montserrat",sans-serif;color:var(--text);background:var(--white);position:relative}
section,footer{position:absolute;left:0;width:1200px}
.abs{position:absolute}
.btn{position:absolute;display:flex;align-items:center;justify-content:center;background:var(--grad);color:var(--white);font-size:12.5px;font-weight:500;height:40px;width:188px}
.btn.pill{border-radius:20px}
.h2{font-weight:500;color:var(--heading);font-size:33px;line-height:47px}
.rule{position:absolute;width:72px;height:2px;background:var(--rule)}
.body-text{font-size:12.5px;line-height:22.5px;color:var(--text)}
.ring{position:absolute;border-radius:50%;background:linear-gradient(160deg,#6a0fd8,#2a7ce6 60%,#fff 85%)}
.photo{position:absolute;border-radius:50%}

/* hero */
.hero{top:0;height:601px}
.hero-photo{position:absolute;inset:0;background:linear-gradient(90deg,#f4f2f1 0%,#f0ece9 35%,#d9cdc4 60%,#b8a89c 78%,#cfc8c2 100%)}
.hero-fade{position:absolute;inset:0;background:linear-gradient(90deg,rgba(255,255,255,.85) 0%,rgba(255,255,255,.6) 40%,rgba(255,255,255,0) 60%)}
.brand{position:absolute;display:flex;align-items:center;gap:8px}
.brand-dot{width:30px;height:30px;border-radius:50%;background:var(--purple)}
.brand-name{font-weight:700;font-size:30px;color:#555}
.hero-title{left:161px;top:190px;font-family:"Roboto Condensed",sans-serif;font-weight:700;font-size:47px;line-height:53px;background:var(--grad);-webkit-background-clip:text;background-clip:text;color:transparent}
.hero-tag{left:163px;top:312px;font-family:"Kaushan Script",cursive;font-size:28px;color:#111}
.btn.sq{border-radius:0}

/* services */
.services{top:1180px;height:546px;background:var(--grey-bg)}
.center-h{left:0;width:1200px;text-align:center}
.svc{position:absolute;width:245px}
.svc-icon{width:58px;height:58px;border-radius:50%;background:#ece6fb}
.svc h3{font-size:15px;font-weight:600;color:#111;margin-top:16px}
.svc p{font-size:12.3px;line-height:21.5px;margin-top:8px}
.svc .more{font-size:12px;font-weight:600;color:#111;margin-top:10px;display:flex;align-items:center;gap:6px}
.svc-card{position:absolute;left:453px;top:174px;width:287px;height:279px;background:var(--white);border-radius:6px;box-shadow:0 2px 10px rgba(0,0,0,.18);overflow:hidden}

/* list */
.ticks{list-style:none}
.ticks li{position:relative;padding-left:28px;font-size:12.3px;line-height:21.5px;margin-bottom:10px}
.ticks svg{position:absolute;left:0;top:3px}

/* testimonials */
.quote{position:absolute;top:210px;width:423px;height:222px;background:var(--white);box-shadow:0 2px 14px rgba(0,0,0,.1);text-align:center;padding:52px 24px 0}
.quote h4{font-size:15px;font-weight:500;color:var(--heading)}
.quote p{font-size:12.2px;line-height:22.5px;margin-top:8px}
.quote .bar{position:absolute;left:18px;right:18px;bottom:0;height:4px;background:var(--grad);border-radius:2px}
.avatar{position:absolute;top:-38px;left:174px;width:76px;height:76px;border-radius:50%;border:2px solid var(--purple);background:linear-gradient(135deg,#e9e4f7,#c9c3d8)}
.arrow{position:absolute;width:38px;height:38px;border-radius:50%;display:flex;align-items:center;justify-content:center;font-size:18px}

/* inquiry */
.map{position:absolute;left:161px;top:118px;width:405px;height:222px;border:6px solid #fff;box-shadow:0 1px 8px rgba(0,0,0,.2);background:linear-gradient(135deg,#e3e3e3,#cfcfcf)}
.contact-item{position:absolute;left:175px;display:flex;align-items:flex-start;gap:16px;font-size:13.5px;line-height:24px;color:#222}
.c-ico{width:32px;height:32px;border-radius:50%;border:1.5px solid #b9a9e0;display:flex;align-items:center;justify-content:center;flex:none}
.field{position:absolute;left:633px;width:404px;border:1px solid #d6d6d6;background:#fff;display:flex;align-items:center;gap:14px;padding:0 14px;font-size:12.5px;color:#222}
.field .req{color:#c00}
.small{font-size:11.5px;color:#222}

/* footer */
footer{top:4104px;height:253px;background:var(--black);color:var(--white)}
</style>
</head>
<body>

<section class="hero">
  <div class="hero-photo" role="img" aria-label="Photo of a smiling couple embracing in a bright home interior"></div>
  <div class="hero-fade"></div>
  <div class="brand" style="left:161px;top:44px">
    <span class="brand-dot"></span><span class="brand-name">VelTra</span>
  </div>
  <div class="btn sq" style="left:851px;top:46px">Request a Consultation</div>
  <h1 class="abs hero-title">The Premier Ketamine<br>Treatment Provider</h1>
  <div class="abs hero-tag">Redefining The Meaning of Happiness</div>
  <div class="btn sq" style="left:161px;top:366px">Request a Consultation</div>
</section>

<section class="about" style="top:601px;height:579px">
  <div class="ring" style="left:161px;top:46px;width:440px;height:434px"></div>
  <div class="photo" style="left:172px;top:46px;width:430px;height:434px;background:linear-gradient(135deg,#d9d6d3,#b8c4d0 55%,#8c7a6a)" role="img" aria-label="Photo of a therapist talking with a young woman on a blue armchair"></div>
  <h2 class="abs h2" style="left:626px;top:112px">About VelTra.com</h2>
  <span class="rule" style="left:628px;top:164px"></span>
  <div class="abs body-text" style="left:628px;top:183px;width:410px">
    <p>Lorem ipsum dolor sit amet, consectetur adipiscing elit. Quisque quis quammu pellentesque dui in varius odio. Nunc convallis bibendum semorttitor tincidunt.</p>
    <p style="margin-top:4px">Vivamus id massa in lectus fringilla interdum et non nisi. tibulum id felislisis sollicitudin ante non, placerat lectus. Lorem ipsu dolor sit amet, consectetur adipiscing elit. Quisque quis pellentesque dui in varius odio convallis.</p>
  </div>
  <div class="btn pill" style="left:628px;top:372px">Request a Consultation</div>
</section>

<section class="services">
  <h2 class="abs h2 center-h" style="top:82px">Our Services</h2>
  <span class="rule" style="left:564px;top:140px"></span>

  <div class="svc" style="left:161px;top:200px">
    <div class="svc-icon" role="img" aria-label="Icon of a head with a brain"></div>
    <h3>Depression</h3>
    <p>Vivamus id massa in lectus fringilla interdum et non nisi. tibulum idlislisis sollicitudin ante non, placerat lectus. Lorem ipsu dolor sit amet...</p>
    <div class="more">Contact Us <svg width="14" height="10" viewBox="0 0 14 10"><path d="M0 5h12M8 1l4 4-4 4" stroke="#111" stroke-width="1.4" fill="none"/></svg></div>
  </div>

  <div class="svc-card">
    <div class="svc" style="left:22px;top:26px">
      <div class="svc-icon" role="img" aria-label="Icon of a worried head"></div>
      <h3>Anxiety</h3>
      <p>Pellentesque et risus nec semismod elementum ornare vel velit. Sedmod enim dolor, nec molestie nunc ibulum vitae. Aenean vestibulum dolor.</p>
    </div>
    <svg class="abs" style="right:0;bottom:0" width="110" height="36" viewBox="0 0 110 36"><defs><linearGradient id="cw" x1="0" x2="1"><stop offset="0" stop-color="#1a8fe6"/><stop offset="1" stop-color="#5a08c2"/></linearGradient></defs><path d="M0 36C30 10 70 0 110 4V36Z" fill="url(#cw)" opacity=".85"/><path d="M30 36C55 18 85 12 110 16V36Z" fill="#7b2ff0"/></svg>
  </div>

  <div class="svc" style="left:795px;top:200px">
    <div class="svc-icon" role="img" aria-label="Icon of a head with a lightning bolt"></div>
    <h3>Migraines</h3>
    <p>Vivamus id massa in lectus fringilla interdum et non nisi. tibulum idlislisis sollicitudin ante non, placerat lectus. Lorem ipsu dolor sit amet...</p>
    <div class="more">Contact Us <svg width="14" height="10" viewBox="0 0 14 10"><path d="M0 5h12M8 1l4 4-4 4" stroke="#111" stroke-width="1.4" fill="none"/></svg></div>
  </div>
</section>

<section class="ketamine" style="top:1726px;height:640px">
  <h2 class="abs h2" style="left:161px;top:154px">About Ketamine<br>IV Infusion Therapy</h2>
  <span class="rule" style="left:163px;top:254px"></span>
  <p class="abs body-text" style="left:163px;top:272px;width:350px">Vivamus id massa in lectus fringilla interdum et non nisi. tibulum id felislisis sollicitudin ante nonerat lectus. Lorem ipsu dolor sit amet onsectetur adipiscing elit. Quisque quis pellentesque dui varus odio convallis. Lorem ipsum dolor sit amet, consectetur adipiscing elit. Quisque quis quammu pellentesque...</p>
  <div class="btn pill" style="left:161px;top:422px">Request a Consultation</div>
  <div class="ring" style="left:601px;top:97px;width:436px;height:434px;background:linear-gradient(200deg,#6a0fd8,#3a2ad6 50%,#fff 80%)"></div>
  <div class="photo" style="left:600px;top:97px;width:426px;height:434px;background:linear-gradient(135deg,#d7d7d5,#9aa0a4 45%,#5c4a40 75%,#e8e8e8)" role="img" aria-label="Photo of two women talking at a table by a window"></div>
</section>

<section class="lorem" style="top:2366px;height:618px;background:var(--grey-bg)">
  <div class="ring" style="left:161px;top:93px;width:440px;height:434px"></div>
  <div class="photo" style="left:172px;top:93px;width:430px;height:434px;background:linear-gradient(180deg,#e9e4e2 0%,#e8c9a6 50%,#a86a33 80%,#4a3325 100%)" role="img" aria-label="Photo of four friends hugging on a hill at sunset"></div>
  <h2 class="abs h2" style="left:626px;top:86px">Lorem Ipsum Dolor Sit<br>Consectetur Adipiscing.<br>Quisque Quis Qua.</h2>
  <span class="rule" style="left:628px;top:237px"></span>
  <ul class="abs ticks" style="left:626px;top:258px;width:412px">
    <li><svg width="14" height="14" viewBox="0 0 14 14"><circle cx="7" cy="7" r="6" stroke="#5a08c2" fill="none" stroke-width="1.2"/><path d="M4 7l2 2 4-4" stroke="#5a08c2" fill="none" stroke-width="1.2"/></svg>Pellentesque et risus nec sem euismod elementum ornare vel velit. Sed euismod enim dolor nec molestie.</li>
    <li><svg width="14" height="14" viewBox="0 0 14 14"><circle cx="7" cy="7" r="6" stroke="#5a08c2" fill="none" stroke-width="1.2"/><path d="M4 7l2 2 4-4" stroke="#5a08c2" fill="none" stroke-width="1.2"/></svg>Fusce porttitor scelerisque fringilla. Nulla orci justo varius ut aliquam eget convallis vitae elit.</li>
    <li><svg width="14" height="14" viewBox="0 0 14 14"><circle cx="7" cy="7" r="6" stroke="#5a08c2" fill="none" stroke-width="1.2"/><path d="M4 7l2 2 4-4" stroke="#5a08c2" fill="none" stroke-width="1.2"/></svg>Pellentesque vehicula lectus a ullamcorper porta. Phasellus dolor leo vulputate id aliquet nec interdum a dui.</li>
    <li><svg width="14" height="14" viewBox="0 0 14 14"><circle cx="7" cy="7" r="6" stroke="#5a08c2" fill="none" stroke-width="1.2"/><path d="M4 7l2 2 4-4" stroke="#5a08c2" fill="none" stroke-width="1.2"/></svg>Praesent ligula sapien, pulvinar sit amet semper at interdum tristique nulla. In pellentesque scelerisque enim.</li>
  </ul>
  <div class="btn pill" style="left:623px;top:487px">Request a Consultation</div>
</section>

<section class="testimonials" style="top:2984px;height:486px">
  <h2 class="abs h2 center-h" style="top:80px">What Patients Are Saying..</h2>
  <span class="rule" style="left:564px;top:136px"></span>
  <div class="arrow" style="left:101px;top:299px;border:1px solid #555;color:#555">&#8249;</div>
  <div class="quote" style="left:161px">
    <div class="avatar" role="img" aria-label="Portrait of the patient"></div>
    <h4>Dana R.</h4>
    <p>Pellentesque sit amet semper sem. Maecenas faucibus enim sem, vel cursus sapien cursus vitae. In euismod nisl quisrtor maximus luctus. Proin justo urna, semper et accumsan at, maximus ut sem. Nam sit amet porttitor est. Ut vel elit lorem. Donec ac metus nisl eget...</p>
    <span class="bar"></span>
  </div>
  <div class="quote" style="left:614px">
    <div class="avatar" role="img" aria-label="Portrait of the patient"></div>
    <h4>Owen T.</h4>
    <p>Pellentesque sit amet semper sem. Maecenas faucibus enim sem, vel cursus sapien cursus vitae. In euismod nisl quisrtor maximus luctus. Proin justo urna, semper et accumsan at, maximus ut sem. Nam sit amet porttitor est. Ut vel elit lorem. Donec ac metus nisl eget...</p>
    <span class="bar"></span>
  </div>
  <div class="arrow" style="left:1061px;top:299px;background:var(--purple);color:#fff">&#8250;</div>
</section>

<section class="inquiry" style="top:3470px;height:634px">
  <h2 class="abs h2 center-h" style="top:24px">Quick Inquiry</h2>
  <span class="rule" style="left:564px;top:82px"></span>
  <div class="map" role="img" aria-label="Map showing the clinic location"></div>
  <h3 class="abs" style="left:176px;top:358px;font-size:19px;font-weight:500;color:var(--heading)">Contact Details</h3>
  <div class="contact-item" style="top:402px"><span class="c-ico"><svg width="14" height="16" viewBox="0 0 14 16"><path d="M7 15s5-5 5-9A5 5 0 0 0 2 6c0 4 5 9 5 9z" stroke="#5a08c2" fill="none" stroke-width="1.3"/><circle cx="7" cy="6" r="1.8" stroke="#5a08c2" fill="none"/></svg></span><span>123 Building Name, Street Name,<br>City Name, State XY-123456</span></div>
  <div class="contact-item" style="top:474px;align-items:center"><span class="c-ico"><svg width="14" height="14" viewBox="0 0 14 14"><path d="M3 1l2 3-1.5 1.5a8 8 0 0 0 5 5L10 9l3 2-1.5 2.5C6 13 1 8 .5 2.5z" stroke="#5a08c2" fill="none" stroke-width="1.2"/></svg></span><span>123 456 7890</span></div>
  <div class="contact-item" style="top:524px;align-items:center"><span class="c-ico"><svg width="15" height="12" viewBox="0 0 15 12"><rect x="1" y="1" width="13" height="10" rx="1" stroke="#5a08c2" fill="none" stroke-width="1.2"/><path d="M1 2l6.5 5L14 2" stroke="#5a08c2" fill="none" stroke-width="1.2"/></svg></span><span>info@veltra.com</span></div>

  <div class="field" style="top:113px;height:51px"><svg width="14" height="15" viewBox="0 0 14 15"><circle cx="7" cy="4.5" r="3.3" stroke="#555" fill="none"/><path d="M1 14c0-3.5 2.7-5.5 6-5.5s6 2 6 5.5z" stroke="#555" fill="none"/></svg><span>Name<span class="req">*</span></span></div>
  <div class="field" style="top:179px;height:51px"><svg width="15" height="12" viewBox="0 0 15 12"><rect x="1" y="1" width="13" height="10" stroke="#555" fill="none"/><path d="M1 2l6.5 5L14 2" stroke="#555" fill="none"/></svg><span>Email<span class="req">*</span></span></div>
  <div class="field" style="top:243px;height:51px"><svg width="14" height="14" viewBox="0 0 14 14"><path d="M3 1l2 3-1.5 1.5a8 8 0 0 0 5 5L10 9l3 2-1.5 2.5C6 13 1 8 .5 2.5z" stroke="#555" fill="none"/></svg><span>Phone</span></div>
  <div class="field" style="top:308px;height:101px;align-items:flex-start;padding-top:16px"><svg width="15" height="14" viewBox="0 0 15 14"><path d="M7.5 1C4 1 1 3.2 1 6c0 1.4.7 2.6 1.8 3.5L2 13l3.6-2c.6.1 1.2.2 1.9.2 3.5 0 6.5-2.3 6.5-5.2S11 1 7.5 1z" stroke="#555" fill="none"/></svg><span>Message</span></div>

  <div class="abs small" style="left:747px;top:428px">Disclaimer&nbsp;&nbsp;&nbsp;|&nbsp;&nbsp;&nbsp;Privacy Policy</div>
  <div class="abs small" style="left:738px;top:457px;display:flex;align-items:center;gap:6px"><span style="width:10px;height:10px;border:1px solid #333;display:inline-block"></span>I Have Read The Disclaimer<span class="req" style="color:#c00">*</span></div>
  <div class="btn pill" style="left:763px;top:494px;width:148px">Send Message</div>
</section>

<footer>
  <div class="brand" style="left:536px;top:98px">
    <span class="brand-dot"></span><span class="brand-name" style="color:#cfcfcf;font-size:34px">VelTra</span>
  </div>
  <div class="abs" style="left:161px;top:192px;width:878px;height:1px;background:#333"></div>
  <div class="abs" style="left:163px;top:216px;font-size:11.5px">Copyright © 2023 VelTra.com. All Rights Reserved.</div>
  <div class="abs" style="left:779px;top:216px;font-size:11.5px;width:260px;text-align:right">Terms and Conditons&nbsp;&nbsp;&nbsp;&nbsp;•&nbsp;&nbsp;&nbsp;&nbsp;Privacy Policy</div>
</footer>

</body>
</html>
```